Broschüren-Design für Wohnungsgesellschaft
Hallo Lukas, die Zusammenarbeit hat richtig Spaß gemacht. Ich empfanf die gedankliche Herangehensweise als sehr professionell, die vielen Varianten waren eine Hilfe mich am Ende doch für meine Bauchentscheidung für die ersten Designvorschläge zu bestätigen. Sie sind ein toller Dienstleister, schnelle Reaktionen, Mitdenken, dabei immer freundlich, auch wenn ich das 4 mal mit dem gleichen Thema kam.
Zielgruppe
wir betreuen im Auftrag der Wohnungsgesellschaften Mieter die ihre Miete oder Mietnebenkosten nicht oder nur teilweise bezahlen.
Ziel ist,in einer telefonischen, email, Whatsapp-Betreuung, den Schuldnern einen Ausweg zu zeigen.
Wir nehmen den Schulder quasi an die Hand um in gemeinsamer Abstimmung d,h, Augenhöhe
Teilzahlungspläne zu erarbeiten und jeweils auch einzuhalten.
Ziel ist es die Würde des Schuldners zu bewahren und der Wohnungsgesellschaft die ihr zustehenden Summen zu sichern.
Das Ganze sehr im Unterschied zu brutalen und teueren Inkasso Aktivitäten einschlägiger Firmen.
Aufgabenstellung
lebendige, freundliche Darstellung, ohne dümmliche Gesichter telfonierender Damen,
plaktiv, doch klar1. die Zielgruppe der Broschüre sind Vorstände und GF größerer Wohnungsgesellschaften.
Diese Menschen haben ein Problem, dass nicht bezahlte Mieten, den Unternehmensertrag und die Liquidität der Gesellschaft negativ beeinflussen.
2. Si3e wollen natürlich die Mieten kassieren, gleichzeitig wollen Sie sich nicht als brutale Geldeintreiber in der Tageszeitung und in den Köpfen aller anderen Mieter wahrgenommen werden.
3. bislang gibt es in jeder Gesellschaft angestellte Mitarbeiter, die meist untrainiert die Beitreibung betreiben. Der Job ist selten gerne übernommen, die Tagesform bestimmt den Ton. Wenn der Mitarbeiter ausfällt ist meist kein Ersatz da.
4. in der Regel startet kurz nach dem Fälligkeitstermin ein automatisiertes schriftliches Mahnverfahren (per Computer) mit 1-3 Stufen, danach wandert das ganze zu professionellen Inkassounternehmen, die dicke Mahngebühren berechnen, den Schuldner bedrohen bis hin zu persönlichen Besuchen, der Gerichtsvollzieher ist dann die noch moderate Form.
5. der BMQ Ansatz will genau das vermeiden, zumindest dort, wo ungeplante Umstände plötzliche Zahlungsengpässe verursachen oder Menschen nicht mit ihrem Geld richtig wirtschaften. Es geht nicht um die notorischen Zahlungsverweigerern.
Die Geschäftsführung der Gesellschaft soll und will das Gefühl haben, dass ihre Mieter auf Augenhöhe behandelt werden und genau deshalb kontinuierlich durch telefonische Ansprache, helfende Führung betreut werden, damit sie dartan arbeiten, die Mietshuld abzutragen und künftige Mieten pünktlich zahlen.
6. das wichtige Mittel ist der partnerschaftlich erstellte Zahlungsplan, der die Zahlungsmöglichkeiten in Raten des Mieters berücksichtig, der Grund ist, dass der Schuldner angesprochen werden kann, z.b. geht die Zahlung ein gelobt wird, kurz vorher an den Zahlungstermin erinn..

```html
<!DOCTYPE html>
<html lang="de">
<head>
<meta charset="utf-8">
<title>BMQ Immobilienservices – Broschüre</title>
<link rel="stylesheet" href="https://fonts.googleapis.com/css2?family=Outfit:wght@300;400;800&display=swap">
<style>
  :root {
    --stage: #a9a9a9;
    --paper: #f4f4f4;
    --paper-edge: #ebebeb;
    --orange: #ee931e;
    --slate: #838687;
    --white: #ffffff;
    --logo-grey: #6f7273;
    --photo-warm: #e9bd84;
    --photo-warm-deep: #d9a563;
    --photo-cool: #c9cbcf;
    --photo-cool-deep: #b4b7bb;
    --photo-tan: #d7a56a;
    --photo-tan-deep: #c58f52;
  }
  * { box-sizing: border-box; margin: 0; padding: 0; }
  html, body { width: 1200px; height: 900px; overflow: hidden; }
  body {
    background: var(--stage);
    font-family: "Outfit", sans-serif;
    position: relative;
  }
  .cover {
    position: absolute;
    left: 60px; top: 60px;
    width: 1080px; height: 780px;
    background: linear-gradient(180deg, var(--paper) 0%, var(--paper-edge) 100%);
    overflow: hidden;
  }
  .photo {
    position: absolute;
    left: 28px;
    width: 219px; height: 226px;
  }
  .photo--house { top: 22px; background: linear-gradient(135deg, var(--photo-warm) 0%, var(--photo-warm-deep) 100%); }
  .photo--phone { top: 272px; background: linear-gradient(135deg, var(--photo-cool) 0%, var(--photo-cool-deep) 100%); }
  .photo--keys  { top: 525px; background: linear-gradient(135deg, var(--photo-tan) 0%, var(--photo-tan-deep) 100%); }

  .brand {
    position: absolute;
    right: 63px; top: 84px;
    display: flex; align-items: center; gap: 8px;
    font-weight: 400;
    font-size: 22px;
    color: var(--logo-grey);
    letter-spacing: 0.2px;
  }
  .brand__mark {
    width: 12px; height: 12px;
    background: var(--orange);
  }

  .headline-band {
    position: absolute;
    left: 337px; top: 310px;
    width: 743px; height: 153px;
    background: var(--orange);
  }
  .headline {
    position: absolute;
    right: 49px; top: 20px;
    text-align: right;
    color: var(--white);
    font-weight: 800;
    font-size: 58px;
    line-height: 55px;
    letter-spacing: -0.5px;
  }

  .answer-panel {
    position: absolute;
    left: 504px; top: 463px;
    width: 576px; height: 317px;
    background: var(--slate);
    color: var(--white);
  }
  .answer-panel__title {
    position: absolute;
    right: 49px; top: 22px;
    font-weight: 800;
    font-size: 62px;
    line-height: 1;
    letter-spacing: -0.5px;
  }
  .answer-panel__text {
    position: absolute;
    right: 49px; top: 90px;
    text-align: right;
    font-weight: 300;
    font-size: 25px;
    line-height: 32px;
  }
  .answer-panel__url {
    position: absolute;
    right: 49px; top: 244px;
    font-weight: 400;
    font-size: 15px;
  }
</style>
</head>
<body>
  <main class="cover">
    <div class="photo photo--house" role="img" aria-label="Zwei Hände schützen ein kleines Holzhaus"></div>
    <div class="photo photo--phone" role="img" aria-label="Smartphone neben einem Stapel Münzen"></div>
    <div class="photo photo--keys" role="img" aria-label="Offene Hand mit Schlüsselbund und Hausanhänger"></div>

    <div class="brand">
      <span class="brand__mark"></span>
      <span class="brand__name">BMQ Immobilienservices</span>
    </div>

    <section class="headline-band">
      <h1 class="headline">Mieter wollen ihre<br>Miete pünktlich zahlen</h1>
    </section>

    <section class="answer-panel">
      <h2 class="answer-panel__title">Stimmt!</h2>
      <p class="answer-panel__text">Manchmal kommt es leider<br>anders Deshalb braucht es ein<br>Optimiertes Mietschuldenmanagement</p>
      <p class="answer-panel__url">www.bmq-immobilienservices.de</p>
    </section>
  </main>
</body>
</html>
```